Kelbrook Training Australia - Course Brochure Design

Kelbrook Training Australia is a Private Register Training Organisation that delivery accredited training courses to students. These courses are delivery via face to face training and distance education (e.g. elearning).

We are looking to get a template designed via adobe in design that we can use for each of our courses and list the information relevant for each one.

It will need to be around 3 - 4 pages long to be able to fit the information required into the brochure, i have attached some example of other providers course information sheets.

From the examples you'll be able to see that most of the information will remained the same until it gets to the course structure.

I would like it to be kept within our current theme, we are in the middle of upgrading our new website and look (www.kelbrook.com.au/drupal).

I look forward to see what you all come back with.

Reason: Hi everyone, Thanks for submitting your design, I have extended the deadline due to not many designs have been submitted. I will be review and providing feedback on the designed submitted this week and will provide some more information based off the work and direction of the designs submitted. Thanks, Ralph.

Target Market(s)

our target market is business and individuals who would like to undergo training course. This brochure needs to display the require information.

Industry/Entity Type

Education

Requirements
Must have
• The brochure must have a front page with a design to list our company logo and information and the course title.

A call to action must be on every page, e.g. footer to enrol now call kelbok on 1800 392 508 or visit www.kelbrook.com.au

Nice to have
• Some picture to fill the pages would add a nice look

```html
<!DOCTYPE html>
<html lang="en">
<head>
<meta charset="utf-8">
<title>Kelbrook Training Australia – Course Structure</title>
<link href="https://fonts.googleapis.com/css2?family=Hind:wght@400;500;600;700&display=swap" rel="stylesheet">
<style>
  :root {
    --backdrop: #e9e6e1;
    --paper: #ffffff;
    --ink: #1e1e1e;
    --heading: #1b4d72;
    --navy: #163f60;
    --footer: #134a6d;
    --gold: #e2aa22;
    --orange: #e07b23;
    --sky: #2f78a6;
    --deep: #1f3c5e;
  }
  * { box-sizing: border-box; margin: 0; padding: 0; }
  html, body { width: 1200px; height: 1140px; overflow: hidden; }
  body {
    background: var(--backdrop);
    font-family: "Hind", Arial, sans-serif;
    color: var(--ink);
    position: relative;
  }
  .page {
    position: absolute;
    left: 205px; top: 16px;
    width: 790px; height: 1108px;
    background: var(--paper);
    box-shadow: 0 4px 18px rgba(0,0,0,.18);
    display: flex; flex-direction: column;
  }
  .colour-bar { display: flex; height: 30px; }
  .colour-bar span { flex: 1; }
  .colour-bar .gold { background: var(--gold); }
  .colour-bar .orange { background: var(--orange); }
  .colour-bar .sky { background: var(--sky); }
  .colour-bar .deep { background: var(--deep); }

  .content { flex: 1; padding: 34px 62px 0; }
  .packaging { font-size: 12.5px; line-height: 1.35; }
  .packaging h2 { font-size: 13px; font-weight: 700; color: var(--heading); }
  .packaging strong { font-weight: 700; }
  .packaging p { margin: 0; }
  .packaging .gap { margin-top: 8px; }

  .feature-photo {
    margin-top: 16px;
    height: 318px;
    border: 9px solid var(--navy);
    background: linear-gradient(160deg, #eef1f4 0%, #d8dde2 45%, #c8b49a 70%, #9aa2a8 100%);
  }

  .units { display: grid; grid-template-columns: 1fr 1fr; gap: 0 34px; margin-top: 20px; }
  .units h3 { font-size: 14px; font-weight: 700; color: var(--heading); margin-top: 12px; line-height: 1.1; }
  .units h4 { font-size: 13.5px; font-weight: 700; color: var(--heading); margin-top: 9px; line-height: 1.1; }
  .units h3 + h4 { margin-top: 2px; }
  .unit { display: grid; grid-template-columns: 92px 1fr; font-size: 13px; line-height: 1.28; margin-top: 1px; }
  .unit .code { letter-spacing: .2px; }
  .units .column > :first-child { margin-top: 0; }

  .footer {
    height: 118px;
    background: var(--footer);
    color: #fff;
    display: flex; align-items: flex-end;
    padding: 0 62px 22px;
    font-size: 16px; font-weight: 500;
  }
  .footer .page-number { margin-right: 14px; }
  .footer .divider { margin-right: 14px; }
</style>
</head>
<body>
  <article class="page">
    <div class="colour-bar">
      <span class="gold"></span><span class="orange"></span><span class="sky"></span><span class="deep"></span>
    </div>

    <div class="content">
      <section class="packaging">
        <h2>Packaging Rules</h2>
        <p><strong>Total number of units = 13</strong></p>
        <p><strong>2 core units</strong> plus</p>
        <p><strong>11 elective</strong> units</p>
        <p><strong>7 elective units</strong> must be selected from the <strong>Group A</strong> units listed below.</p>
        <p class="gap">The remaining <strong>4 elective units</strong> may be selected from the <strong>Group A</strong> or <strong>Group B</strong> elective units listed below, or any currently endorsed Training Package or accredited course at the same qualification level. If not listed below <strong>2 of the electives units</strong> may be selected from a Certificate II or Certificate IV qualification.</p>
      </section>

      <div class="feature-photo" role="img" aria-label="Photo of a smiling team meeting around an office table"></div>

      <section class="units">
        <div class="column">
          <h3>Core Units</h3>
          <h4>IT Use</h4>
          <div class="unit"><span class="code">BSBITU307A</span><span>Develop keyboarding speed and accuracy</span></div>
          <h4>Occupational Health and Safety</h4>
          <div class="unit"><span class="code">BSBOHS201A</span><span>Participate in OHS processes</span></div>

          <h3>Elective units</h3>
          <h3>Group A units</h3>
          <h4>Financial Administration</h4>
          <div class="unit"><span class="code">BSBFIA302A</span><span>Process payroll</span></div>
          <div class="unit"><span class="code">BSBFIA303A</span><span>Process accounts payable and receivable</span></div>
          <div class="unit"><span class="code">BSBFIA304A</span><span>Maintain a general ledger</span></div>
          <h4>General Administration</h4>
          <div class="unit"><span class="code">BSBADM307B</span><span>Organise schedules</span></div>
          <h4>IT Use</h4>
          <div class="unit"><span class="code">BSBITU302B</span><span>Create electronic presentations</span></div>
          <div class="unit"><span class="code">BSBITU303A</span><span>Design and produce text documents</span></div>
          <div class="unit"><span class="code">BSBITU304A</span><span>Produce spreadsheets</span></div>
          <div class="unit"><span class="code">BSBITU306A</span><span>Design and produce business documents</span></div>
          <div class="unit"><span class="code">BSBITU309A</span><span>Produce desktop published documents</span></div>
        </div>

        <div class="column">
          <h4>Writing</h4>
          <div class="unit"><span class="code">BSBWRT301A</span><span>Write simple documents</span></div>
          <h3>Group B units</h3>
          <h4>Customer Service</h4>
          <div class="unit"><span class="code">BSBCUS301B</span><span>Deliver and monitor a service to customers</span></div>
          <h4>Diversity</h4>
          <div class="unit"><span class="code">BSBDIV301A</span><span>Work effectively with diversity</span></div>
          <h4>Financial Administration</h4>
          <div class="unit"><span class="code">BSBFIA301A</span><span>Maintain financial records</span></div>
          <h4>General Administration</h4>
          <div class="unit"><span class="code">BSBADM302B</span><span>Produce texts from notes</span></div>
          <div class="unit"><span class="code">BSBADM303B</span><span>Produce texts from audio transcription</span></div>
          <div class="unit"><span class="code">BSBADM311A</span><span>Maintain business resources</span></div>
          <h4>Information Management</h4>
          <div class="unit"><span class="code">BSBINM301A</span><span>Organise workplace information</span></div>
          <div class="unit"><span class="code">BSBINM302A</span><span>Utilise a knowledge management system</span></div>
          <div class="unit"><span class="code">BSBINM303A</span><span>Handle receipt and despatch of information</span></div>
        </div>
      </section>
    </div>

    <footer class="footer">
      <span class="page-number">4</span><span class="divider">|</span>
      <span class="call-to-action">To enrol now call kelbok on 1800 392 508 or visit www.kelbrook.com.au</span>
    </footer>
  </article>
</body>
</html>
```